Addiction Treatment and Mental Health Center needs a brochure

Our company is called, Willowmere House Islamabad, and it is a private, upscale addiction recovery and mental health facility that provides comprehensive client-centred treatment and support for individuals and their families. We provide both short-term and long-term residential treatment, outpatient services, continuing care, and family support. We strive to offer the highest quality standards of care through implementing innovative and evidence-based treatment programs, quality control measures, and ethical decision making protocols. Our treatment style is holistic and incorporates modern medicine and therapies along with complimentary and alternative healing therapies. We also distinguish ourselves by offering a treatment environment that is open, green and and serene. We would like to see a brochure design that reflects these elements and our approach to treatment.
Requirements
Must have
- Tri-fold pamphlet

```html
<!DOCTYPE html>
<html lang="en">
<head>
<meta charset="utf-8">
<title>Willowmere House Islamabad – Tri-fold Brochure</title>
<link href="https://fonts.googleapis.com/css2?family=Montserrat:wght@300;400;500;600;700;800&display=swap" rel="stylesheet">
<style>
:root{
  --page:#ececec;
  --paper:#ffffff;
  --blue:#1652a5;
  --blue-bright:#1e7fd3;
  --sky:#5fc0ee;
  --green:#76c043;
  --pale-blue:#c4e5f8;
  --ink:#3b3b3b;
  --muted:#555555;
  --orange:#f7941d;
  --white:#ffffff;
}
*{box-sizing:border-box;margin:0;padding:0}
html,body{width:941px;height:1200px;overflow:hidden}
body{background:var(--page);font-family:"Montserrat",sans-serif;color:var(--ink);position:relative}
.sheet{position:absolute;left:91px;width:758px;height:540px;background:var(--paper);overflow:hidden;box-shadow:0 2px 8px rgba(0,0,0,.12)}
.sheet--outside{top:53px}
.sheet--inside{top:624px}
.panel{position:absolute;top:0;height:540px;overflow:hidden}
.abs{position:absolute}
.heading{position:absolute;font-weight:700;color:var(--blue);font-size:15px;white-space:nowrap;display:flex;align-items:center}
.heading::after{content:"";display:inline-block;width:22px;height:1px;background:var(--orange);margin-left:5px}
.body-copy{position:absolute;font-weight:300;font-size:6.6px;line-height:11.5px;color:var(--muted);letter-spacing:-.05px}
.photo{position:absolute;border-radius:16px}
.brand-name{font-weight:500;white-space:nowrap;letter-spacing:-.2px}
.brand-tag{font-weight:500;letter-spacing:2px;white-space:nowrap}
/* outside: contact */
.contact-label{position:absolute;font-size:7.4px;font-weight:400;color:var(--muted);display:flex;align-items:center}
.contact-label::after{content:"";display:inline-block;width:14px;height:1px;background:var(--orange);margin-left:4px}
.contact-line{position:absolute;left:277px;font-size:9.2px;color:var(--ink);display:flex;align-items:center;gap:4px;white-space:nowrap}
.contact-line svg{width:7px;height:7px;flex:none}
.contact-line--bold{font-weight:700;font-size:9px}
.social-dot{width:7px;height:7px;border-radius:50%;background:var(--blue-bright);flex:none}
/* inside: services */
.service{position:absolute;width:200px}
.service__icon{position:absolute;left:0;top:0;width:41px;height:41px;border-radius:50%;padding:2px;background:linear-gradient(135deg,var(--blue-bright),var(--green))}
.service__icon span{display:block;width:100%;height:100%;border-radius:50%;border:2px solid var(--white)}
.service__title{position:absolute;left:46px;top:0;font-size:9.4px;font-weight:700;color:#222;white-space:nowrap}
.service__text{position:absolute;left:46px;top:12px;width:168px;font-size:7px;line-height:10.4px;font-weight:400;color:var(--muted)}
</style>
</head>
<body>

<!-- OUTSIDE SPREAD -->
<section class="sheet sheet--outside">

  <!-- inner flap -->
  <div class="panel" style="left:0;width:255px">
    <svg class="abs" style="left:0;top:0" width="255" height="540" viewBox="0 0 255 540">
      <path d="M0 405 C40 420 120 430 200 440 C240 448 255 480 255 540 L0 540 Z" fill="var(--pale-blue)"/>
    </svg>
    <h2 class="heading" style="left:29px;top:31px">Our Facility</h2>
    <p class="body-copy" style="left:29px;top:50px;width:208px">At Willowmere House we understand that a comfortable, relaxing and safe physical environment is integral to treating our clients and helping them in their recovery process. We go to great lengths to ensure that our clients are provided with high quality amenities along with an environment that fosters healing.</p>
    <h2 class="heading" style="left:29px;top:134px">Residence</h2>
    <p class="body-copy" style="left:29px;top:153px;width:208px">We offer separate residential treatment for both men and women. Our facility has both private and shared rooms, that are designed for comfort and privacy. We have both in-door and out-door lounge areas for group activities, a communal garden, and a beautiful green space where our clients can take part in physical activities and spend their time in leisure.</p>
    <h2 class="heading" style="left:29px;top:239px">Meals</h2>
    <p class="body-copy" style="left:29px;top:258px;width:208px">We prioritize healthy eating by offering freshly prepared gourmet meals, with a preference for local, organic products and in-season produce. We also accommodate dietary needs including food allergies and intolerances, as well as religious restrictions.</p>
    <h2 class="heading" style="left:29px;top:332px">Security</h2>
    <p class="body-copy" style="left:29px;top:351px;width:208px">Our center is staffed twenty-four hours a day and we provide around the clock security and surveillance so that our clients and their loved ones feel safe and have peace of mind during their stay with us.</p>
    <div class="photo" role="img" aria-label="Man with arms spread wide under a clear blue sky" style="left:31px;top:414px;width:201px;height:101px;border-radius:16px 40px 0 16px;background:linear-gradient(180deg,#2f72b8 0%,#5d9ad2 60%,#c9d8e2 100%)"></div>
  </div>

  <!-- back panel -->
  <div class="panel" style="left:255px;width:247px">
    <svg class="abs" style="left:0;top:0" width="247" height="540" viewBox="0 0 247 540">
      <defs>
        <linearGradient id="backTop" x1="0" y1="0" x2="0" y2="1">
          <stop offset="0" stop-color="#1a63b0"/><stop offset="1" stop-color="#3b9be0"/>
        </linearGradient>
      </defs>
      <path d="M0 0 H247 V310 L70 310 C25 310 0 290 0 230 Z" fill="url(#backTop)"/>
      <path d="M0 200 C0 270 20 305 60 315 C25 300 4 265 2 200 Z" fill="var(--green)"/>
    </svg>
    <div class="abs" role="img" aria-label="Faded photo of the centre's columned entrance" style="left:0;top:0;width:247px;height:230px;background:linear-gradient(180deg,rgba(255,255,255,.12),rgba(255,255,255,0))"></div>
    <div class="abs" style="left:0;top:113px;width:247px;text-align:center;color:var(--white)">
      <div class="brand-name" style="font-size:10.5px">Willowmere House Islamabad</div>
      <div class="brand-tag" style="font-size:5.4px;margin-top:2px">REHAB &amp; WELLNESS CENTER</div>
    </div>
    <p class="abs" style="left:0;top:155px;width:247px;text-align:center;color:var(--white);font-size:10px;font-weight:300;line-height:16px">House 24, 310 Rd,<br>Cedar Lane St, Bani Gala, Islamabad</p>
    <div class="abs" role="img" aria-label="Street map showing the centre's location in Bani Gala" style="left:34px;top:203px;width:181px;height:163px;border-radius:12px 30px 0 30px;background:linear-gradient(135deg,#f2f3f5,#e3e6ea);box-shadow:0 4px 10px rgba(0,0,0,.12)"></div>
    <div class="contact-label" style="left:22px;top:390px">Make an Appointment</div>
  </div>
  <div class="contact-line contact-line--bold" style="top:405px">
    <svg viewBox="0 0 10 10"><path d="M2 0.6 L3.6 0.6 L4.2 3 L3 3.8 C3.6 5.2 4.8 6.4 6.2 7 L7 5.8 L9.4 6.4 L9.4 8 C9.4 8.8 8.8 9.4 8 9.4 C4 9 1 6 0.6 2 C0.6 1.2 1.2 0.6 2 0.6 Z" fill="var(--blue-bright)"/></svg>
    051 555 0142 <span style="font-weight:300">|</span> 0300-5550187 <span style="font-weight:300">|</span> 0311-5550263
  </div>
  <div class="contact-line" style="top:423px">
    <svg viewBox="0 0 10 10"><rect x="0.5" y="1.5" width="9" height="7" rx="1" fill="var(--blue-bright)"/><path d="M0.8 2 L5 5.4 L9.2 2" stroke="#fff" stroke-width="0.9" fill="none"/></svg>
    hello@willowmerehouse.pk
  </div>
  <div class="contact-line" style="top:440px">
    <svg viewBox="0 0 10 10"><circle cx="5" cy="5" r="4.3" fill="none" stroke="var(--blue-bright)" stroke-width="0.9"/><ellipse cx="5" cy="5" rx="1.8" ry="4.3" fill="none" stroke="var(--blue-bright)" stroke-width="0.8"/><path d="M0.7 5 H9.3" stroke="var(--blue-bright)" stroke-width="0.8"/></svg>
    www.willowmerehouseisb.com
  </div>
  <div class="contact-label" style="left:277px;top:470px">Follow us</div>
  <div class="contact-line" style="top:484px"><span class="social-dot"></span>willowmerehouseisb</div>
  <div class="contact-line" style="top:501px"><span class="social-dot"></span>willowmerehouseislamabad</div>

  <!-- cover panel -->
  <div class="panel" style="left:502px;width:256px">
    <div class="abs" role="img" aria-label="Young man with eyes closed and arms open, breathing in fresh air" style="left:0;top:0;width:256px;height:340px;background:linear-gradient(160deg,#2aa3dd 0%,#3fb1c8 45%,#5cb86a 80%,#76c043 100%)"></div>
    <svg class="abs" style="left:0;top:0" width="256" height="540" viewBox="0 0 256 540">
      <defs>
        <linearGradient id="coverBand" x1="0" y1="0" x2="1" y2="0">
          <stop offset="0" stop-color="#1765b5"/><stop offset=".6" stop-color="#5cc3ee"/><stop offset="1" stop-color="#76c043"/>
        </linearGradient>
      </defs>
      <path d="M0 330 C80 318 160 310 215 330 C240 340 252 360 256 380 L256 540 L0 540 Z" fill="var(--blue-bright)"/>
      <path d="M0 337 C80 326 160 320 210 340 C235 350 248 368 256 390 L256 540 L0 540 Z" fill="var(--white)"/>
      <path d="M5 540 C10 525 25 520 60 520 L256 520 L256 540 Z" fill="url(#coverBand)"/>
    </svg>
    <h1 class="abs" style="left:18px;top:208px;width:230px;color:var(--white);font-size:19.5px;font-weight:800;line-height:24.3px;letter-spacing:.2px">Residential Medical Detox &amp; Addiction Treatment Center</h1>
    <div class="abs" style="left:0;top:438px;width:256px;text-align:center">
      <div class="brand-name" style="font-size:12.5px;color:#2b2b2b">Willowmere House Islamabad</div>
      <div class="brand-tag" style="font-size:6.8px;color:#2b2b2b;margin-top:2px">REHAB &amp; WELLNESS CENTER</div>
    </div>
    <div class="abs" style="left:0;top:487px;width:256px;text-align:center;font-size:10.5px;color:var(--blue-bright)">www.WillowmereHouseISB.com</div>
  </div>
</section>

<!-- INSIDE SPREAD -->
<section class="sheet sheet--inside">

  <!-- left panel -->
  <div class="panel" style="left:0;width:255px">
    <svg class="abs" style="left:0;top:0" width="255" height="540" viewBox="0 0 255 540">
      <defs>
        <linearGradient id="paleFade" x1="0" y1="0" x2="1" y2="0">
          <stop offset="0" stop-color="#cbe9fa"/><stop offset="1" stop-color="#b3def6"/>
        </linearGradient>
      </defs>
      <path d="M0 250 L0 540 L255 540 L255 370 C235 340 200 330 150 330 C80 330 30 300 0 250 Z" fill="url(#paleFade)"/>
    </svg>
    <div class="abs" style="left:29px;top:49px">
      <div class="brand-name" style="font-size:12px;color:#2b2b2b">Willowmere House Islamabad</div>
      <div class="brand-tag" style="font-size:6.3px;color:#2b2b2b;margin-top:1px;padding-left:20px">REHAB &amp; WELLNESS CENTER</div>
    </div>
    <h2 class="heading" style="left:29px;top:98px">About Us</h2>
    <p class="body-copy" style="left:29px;top:119px;width:208px">Willowmere House is a private, upscale addiction recovery and mental health facility that provides comprehensive client-centred treatment and support for individuals and their families. We offer a broad range of clinical care services including both short-term and long-term residential treatment, outpatient services, continuing care, and family support. We use a holistic treatment model, adapting our programs to the needs of the people we serve, in order to promote healthy integration of the mind, body and spirit.</p>
    <div class="photo" role="img" aria-label="Exterior of the two-storey residence with green railings and lawn" style="left:29px;top:248px;width:197px;height:105px;border-radius:0 16px 16px 16px;background:linear-gradient(180deg,#bcd7ec 0%,#e8dcc0 45%,#d8c6a0 75%,#6e9a45 100%)"></div>
    <svg class="abs" style="left:29px;top:248px" width="22" height="22" viewBox="0 0 22 22"><path d="M0 0 H22 L0 22 Z" fill="var(--orange)"/></svg>
    <h2 class="heading" style="left:29px;top:375px">What Distinguishes Us</h2>
    <p class="body-copy" style="left:29px;top:399px;width:208px">At Willowmere House, we strive to offer the highest quality standards of care through implementing innovative and evidence-based treatment programs, quality control measures, and ethical decision making protocols. Our team of highly experienced counsellors, medical specialists, therapists, psychiatrists and support staff are dedicating to ensuring that our clients receive the help they need in an environment that is professional, client-centred, compassionate, non-judgemental, and inclusive.</p>
  </div>

  <!-- center + right panels -->
  <div class="panel" style="left:255px;width:503px">
    <svg class="abs" style="left:0;top:0" width="503" height="540" viewBox="0 0 503 540">
      <defs>
        <linearGradient id="spreadTop" x1="0" y1="0" x2="1" y2="0.4">
          <stop offset="0" stop-color="#2e86d6"/><stop offset=".45" stop-color="#5fc0ee"/><stop offset="1" stop-color="#8fcf6c"/>
        </linearGradient>
      </defs>
      <rect width="503" height="540" fill="url(#spreadTop)"/>
      <path d="M0 70 C0 170 40 235 130 240 L300 240 C400 240 480 220 503 210 L503 540 L0 540 Z" fill="var(--white)"/>
      <line x1="242" y1="0" x2="242" y2="540" stroke="rgba(0,0,0,.04)" stroke-width="1"/>
    </svg>
    <div class="photo" role="img" aria-label="Columned front porch of the residence" style="left:15px;top:40px;width:184px;height:188px;border-radius:16px 30px 30px 16px;background:linear-gradient(180deg,#c9dff0 0%,#e9ddc2 35%,#cdb68d 70%,#a99a86 100%)"></div>
    <div class="photo" role="img" aria-label="Bedroom with a double bed and patterned rug" style="left:200px;top:140px;width:130px;height:114px;border-radius:30px 0 16px 0;background:linear-gradient(180deg,#f0ece6 0%,#dcd4cb 45%,#6d4c3a 80%,#8c6e55 100%);box-shadow:0 3px 8px rgba(0,0,0,.15)"></div>
    <div class="photo" role="img" aria-label="Garden path lined with flowers and trees" style="left:307px;top:58px;width:145px;height:128px;border-radius:30px 0 30px 0;background:linear-gradient(180deg,#9fc7e6 0%,#5f8f44 40%,#b9ae98 70%,#6fa04a 100%)"></div>

    <h2 class="heading" style="left:15px;top:247px;font-size:14.5px">What We Offer</h2>
    <p class="body-copy" style="left:15px;top:270px;width:450px;font-size:7px;line-height:10.6px;font-weight:400">Getting help for a substance use disorder is one of the most important and difficult decisions made by clients and their families. At Willowmere House, we believe that alcoholism and drug addiction are treatable illnesses that clients can recover from. We strive to offer high quality recovery programs that are accessible and affordable. This includes a full spectrum of programs for alcohol, illicit drugs, and nicotine addiction.</p>

    <div class="service" style="left:15px;top:325px">
      <div class="service__icon"><span role="img" aria-label="Hands holding medication" style="background:linear-gradient(135deg,#f1e6dc,#c9a58a)"></span></div>
      <div class="service__title">Medical Detoxification</div>
      <p class="service__text">The goal of our medical detox program is to ensure a safe recovery and minimize discomfort and withdrawal symptoms</p>
    </div>
    <div class="service" style="left:15px;top:388px">
      <div class="service__icon"><span role="img" aria-label="Doctor consulting with a patient" style="background:linear-gradient(135deg,#e6eef5,#9fb7cc)"></span></div>
      <div class="service__title">Inpatient Treatment</div>
      <p class="service__text">We provide a comprehensive and integrative medical and holistic inpatient program with individualized treatment.</p>
    </div>
    <div class="service" style="left:15px;top:450px">
      <div class="service__icon"><span role="img" aria-label="Group support session" style="background:linear-gradient(135deg,#e8d9cc,#a88a74)"></span></div>
      <div class="service__title">Outpatient Treatment</div>
      <p class="service__text">Our outpatient treatment program provides the ongoing support necessary for personal development and healing.</p>
    </div>

    <div class="service" style="left:254px;top:319px">
      <div class="service__icon"><span role="img" aria-label="Doctors reviewing notes together" style="background:linear-gradient(135deg,#eef3f7,#a9bfd3)"></span></div>
      <div class="service__title">Dual Diagnosis Treatment</div>
      <p class="service__text" style="top:10px;line-height:9.8px;width:172px">We understand the relationship between substance abuse and mental health, and our health team employs integrative treatment protocols in order to ensure that our clients receive the right diagnosis and treatment.</p>
    </div>
    <div class="service" style="left:254px;top:389px">
      <div class="service__icon"><span role="img" aria-label="Laser therapy applied to a hand" style="background:linear-gradient(135deg,#cfd6dc,#5d6a75)"></span></div>
      <div class="service__title">Smoking Cessation &amp; Laser Therapy</div>
      <p class="service__text" style="top:10px;line-height:9.8px;width:172px">We specialize in low-level laser therapy (LLLT) for smoking cessation, and stress and anxiety management. Our smoking cessation program is all natural, and helps clients rejuvenate their health and quit smoking within just three sessions.</p>
    </div>
    <div class="service" style="left:254px;top:461px">
      <div class="service__icon"><span role="img" aria-label="Woman meditating" style="background:linear-gradient(135deg,#f3ece4,#c8a98f)"></span></div>
      <div class="service__title">Yoga &amp; Mindfulness</div>
      <p class="service__text" style="top:10px;line-height:9.8px;width:172px">Our mindfulness and yoga therapy program specializes in working with addiction recovery patients in order to help them develop stress management skills and cultivate durable changes in their lives.</p>
    </div>
  </div>
</section>

</body>
</html>
```